K&R Security Services PTY. LTD.

Ive just had my logo made and I'm looking for some simple but strong designs for my business cards the company is a security company.

Please use dark colors.

Regards,

Owen Deloit

Reason: Need more time for discussion with other directors

Industry/Entity Type

Security

Font styles to use
Sans Serif
Decorative

```html
<!DOCTYPE html>
<html lang="en">
<head>
<meta charset="utf-8">
<title>K&amp;R Security Services – Business Card</title>
<link rel="stylesheet" href="https://fonts.googleapis.com/css2?family=Oswald:wght@600;700&family=Marcellus&family=Open+Sans:wght@400&display=swap">
<style>
  :root {
    --bg: #d9d6d2;
    --ink: #2e2e2e;
    --black: #0b0b0b;
    --black-soft: #161616;
    --white: #ffffff;
    --grey: #b9b9b9;
    --rule: #e6e6e6;
  }
  * { box-sizing: border-box; margin: 0; padding: 0; }
  html, body {
    width: 1200px; height: 1200px; overflow: hidden;
    background: var(--bg);
  }
  .canvas { position: relative; width: 1200px; height: 1200px; }

  .card {
    position: absolute; left: 180px; width: 840px; height: 522px;
    overflow: hidden;
    box-shadow: 0 6px 18px rgba(0,0,0,.25);
  }
  .card--front { top: 60px; background: linear-gradient(180deg, var(--black-soft), var(--black)); }
  .card--back {
    top: 618px;
    background: radial-gradient(ellipse 62% 70% at 50% 50%, #ffffff 0%, #e9e9e9 14%, #9a9a9a 34%, #3a3a3a 58%, #0d0d0d 82%);
  }

  .header-band { position: absolute; inset: 0 0 auto 0; height: 210px; }
  .header-band svg { display: block; }

  .brand-mark {
    position: absolute; left: 48px; top: 52px;
    display: flex; align-items: center; gap: 10px;
    font-family: "Oswald", sans-serif; font-weight: 700;
    font-size: 26px; color: var(--ink); letter-spacing: .5px;
  }
  .brand-mark__square { width: 16px; height: 16px; background: var(--ink); }

  .company-title {
    position: absolute; left: 250px; right: 40px; top: 20px;
    font-family: "Oswald", sans-serif; font-weight: 700;
    font-size: 42px; line-height: 46px; color: var(--ink);
    text-align: center; letter-spacing: .5px;
  }

  .person { position: absolute; left: 68px; top: 300px; text-align: center; }
  .person__name {
    font-family: "Marcellus", serif; font-size: 30px; color: var(--white);
    letter-spacing: 1.5px;
  }
  .person__role {
    font-family: "Marcellus", serif; font-size: 22px; color: var(--grey);
    letter-spacing: 1.5px; margin-top: 2px;
  }

  .divider {
    position: absolute; left: 392px; top: 216px; width: 2px; height: 257px;
    background: var(--rule);
  }

  .contact { position: absolute; left: 448px; top: 250px; list-style: none; }
  .contact__item {
    display: flex; align-items: flex-start; gap: 16px;
    font-family: "Open Sans", sans-serif; font-size: 18px; line-height: 30px;
    color: var(--white);
  }
  .contact__item--address { margin-bottom: 8px; }
  .contact__icon { width: 22px; height: 22px; margin-top: 4px; flex: none; }

  .back-mark {
    position: absolute; inset: 0;
    display: flex; align-items: center; justify-content: center; gap: 14px;
    font-family: "Oswald", sans-serif; font-weight: 700;
    font-size: 54px; color: var(--ink); letter-spacing: 1px;
  }
  .back-mark__square { width: 26px; height: 26px; background: var(--ink); }
</style>
</head>
<body>
<main class="canvas">

  <section class="card card--front">
    <div class="header-band">
      <svg width="840" height="210" viewBox="0 0 840 210">
        <path d="M0 0 H840 V150 H250 L238 162 H0 Z" fill="var(--white)"/>
        <path d="M236 180 L254 162 H840" fill="none" stroke="var(--white)" stroke-width="3"/>
      </svg>
    </div>

    <div class="brand-mark">
      <span class="brand-mark__square"></span>
      <span>K&amp;R</span>
    </div>

    <h1 class="company-title">K&amp;R SECURITY SERVICES<br>PTY. LTD.</h1>

    <div class="person">
      <p class="person__name">OWEN DELOIT</p>
      <p class="person__role">PRESIDENT</p>
    </div>

    <div class="divider"></div>

    <ul class="contact">
      <li class="contact__item contact__item--address">
        <svg class="contact__icon" viewBox="0 0 22 22"><rect width="22" height="22" fill="var(--white)"/><path d="M11 4a5 5 0 0 0-5 5c0 4 5 9 5 9s5-5 5-9a5 5 0 0 0-5-5zm0 7a2 2 0 1 1 0-4 2 2 0 0 1 0 4z" fill="var(--black)"/></svg>
        <span>Address Line 1,Address Line 2<br>Address Line 3City,State 555</span>
      </li>
      <li class="contact__item">
        <svg class="contact__icon" viewBox="0 0 22 22"><rect width="22" height="22" fill="var(--white)"/><path d="M4 8c0-2 3-3 7-3s7 1 7 3v1h-4V7.5H8V9H4zM6 10h10l1 7H5z" fill="var(--black)"/><circle cx="11" cy="13.5" r="2" fill="var(--white)"/></svg>
        <span>015550182</span>
      </li>
      <li class="contact__item">
        <svg class="contact__icon" viewBox="0 0 22 22"><rect width="22" height="22" fill="var(--white)"/><rect x="4" y="9" width="14" height="9" fill="var(--black)"/><rect x="7" y="4" width="8" height="5" fill="none" stroke="var(--black)" stroke-width="1.5"/><rect x="7" y="12" width="8" height="1.5" fill="var(--white)"/></svg>
        <span>015550193</span>
      </li>
      <li class="contact__item">
        <svg class="contact__icon" viewBox="0 0 22 22"><rect x="2" y="5" width="18" height="12" fill="none" stroke="var(--white)" stroke-width="1.8"/><path d="M2 5l9 7 9-7M2 17l6-6M20 17l-6-6" fill="none" stroke="var(--white)" stroke-width="1.5"/></svg>
        <span>info@krsecurity.example</span>
      </li>
      <li class="contact__item">
        <svg class="contact__icon" viewBox="0 0 22 22"><g fill="none" stroke="var(--white)" stroke-width="1.5"><circle cx="11" cy="11" r="9"/><ellipse cx="11" cy="11" rx="4" ry="9"/><path d="M2 11h18M4 6h14M4 16h14"/></g></svg>
        <span>WWW.krsecurity.example</span>
      </li>
    </ul>
  </section>

  <section class="card card--back">
    <div class="back-mark">
      <span class="back-mark__square"></span>
      <span>K&amp;R</span>
    </div>
  </section>

</main>
</body>
</html>
```